Design for product lable
MERO LUX
COMMING SOON
background design for nutrition products
such as whey protein powders Cretin and so on
this well be our background style
all the fallowing products gonna look nearly the same so the wining design well work on all other products we produce background our bottle color is black we have blue and gold on our logo
athlete, mostly fitness and bodybuilders
and all others sports
it must come in 4 flavor variants : chocolate, vanilla, strawberry,banana
pleas avoid using to many braid colors
try to give a royal look to it thank you
remember it is 250 because separately for each product if you are a wining project then we make a deal what we gonna pay for the each fallowing product
amino profile total hight 6cm
weight 12 cm
color wight or must much whit the label color or whit background blact text
this is a bad resolution so pleas make new charts

```html
<!DOCTYPE html>
<html lang="en">
<head>
<meta charset="utf-8">
<title>MERO LUX – Flavour Lid Labels</title>
<link rel="stylesheet" href="https://fonts.googleapis.com/css2?family=Cinzel:wght@700&family=Montserrat:wght@400;600&display=swap">
<style>
  :root {
    --bg: #1c1c1e;
    --text-light: #ffffff;
    --text-soft: rgba(255,255,255,0.82);
    --choc-rim: #7a3f1c;
    --choc-face: #4a2412;
    --choc-deep: #1e0d06;
    --vanilla-rim: #1d3fc0;
    --vanilla-face: #13288a;
    --vanilla-deep: #060d33;
    --banana-rim: #d8a514;
    --banana-face: #8a6a0a;
    --banana-deep: #2e2303;
    --straw-rim: #c8141f;
    --straw-face: #8a0d14;
    --straw-deep: #2e0306;
    --brand-accent: #e0a93a;
  }
  * { margin: 0; padding: 0; box-sizing: border-box; }
  html, body {
    width: 1200px;
    height: 901px;
    overflow: hidden;
    background: var(--bg);
  }
  .label-sheet {
    width: 1200px;
    height: 901px;
    display: grid;
    grid-template-columns: repeat(2, 420px);
    grid-template-rows: repeat(2, 420px);
    justify-content: center;
    align-content: center;
    gap: 20px 120px;
  }
  .lid-label {
    width: 420px;
    height: 420px;
    border-radius: 50%;
    padding: 22px;
    background: radial-gradient(circle at 35% 25%, rgba(255,255,255,0.35), transparent 55%), var(--rim);
    box-shadow: inset 0 0 0 3px rgba(0,0,0,0.35);
  }
  .lid-face {
    width: 100%;
    height: 100%;
    border-radius: 50%;
    background:
      radial-gradient(circle at 50% 40%, var(--face) 0%, var(--deep) 80%);
    box-shadow: inset 0 0 0 2px rgba(255,255,255,0.15);
    display: flex;
    flex-direction: column;
    align-items: center;
    justify-content: center;
    text-align: center;
    color: var(--text-light);
    font-family: "Montserrat", sans-serif;
  }
  .maker {
    display: flex;
    align-items: center;
    gap: 8px;
    font-family: "Montserrat", sans-serif;
    font-weight: 600;
    font-size: 15px;
    letter-spacing: 3px;
    color: var(--brand-accent);
    margin-bottom: 6px;
  }
  .maker-dot {
    width: 10px;
    height: 10px;
    border-radius: 50%;
    background: var(--brand-accent);
  }
  .product-name {
    font-family: "Cinzel", serif;
    font-weight: 700;
    font-size: 58px;
    line-height: 1;
    letter-spacing: 1px;
  }
  .tagline {
    margin-top: 10px;
    font-size: 11px;
    letter-spacing: 1.5px;
    text-transform: uppercase;
    color: var(--text-soft);
  }
  .divider {
    width: 220px;
    height: 1px;
    margin: 12px 0 10px;
    background: rgba(255,255,255,0.4);
  }
  .flavour {
    font-size: 17px;
    font-weight: 400;
    letter-spacing: 1px;
  }
  .chocolate { --rim: var(--choc-rim); --face: var(--choc-face); --deep: var(--choc-deep); }
  .vanilla { --rim: var(--vanilla-rim); --face: var(--vanilla-face); --deep: var(--vanilla-deep); }
  .banana { --rim: var(--banana-rim); --face: var(--banana-face); --deep: var(--banana-deep); }
  .strawberry { --rim: var(--straw-rim); --face: var(--straw-face); --deep: var(--straw-deep); }
</style>
</head>
<body>
  <main class="label-sheet">
    <section class="lid-label chocolate">
      <div class="lid-face">
        <div class="maker"><span class="maker-dot"></span>VERAFORM</div>
        <h1 class="product-name">MEROLUX</h1>
        <p class="tagline">Pure Whey Protein Isolate Blend</p>
        <div class="divider"></div>
        <p class="flavour">Double Rich Chocolate</p>
      </div>
    </section>
    <section class="lid-label vanilla">
      <div class="lid-face">
        <div class="maker"><span class="maker-dot"></span>VERAFORM</div>
        <h2 class="product-name">MEROLUX</h2>
        <p class="tagline">Pure Whey Protein Isolate Blend</p>
        <div class="divider"></div>
        <p class="flavour">Vanilla</p>
      </div>
    </section>
    <section class="lid-label banana">
      <div class="lid-face">
        <div class="maker"><span class="maker-dot"></span>VERAFORM</div>
        <h2 class="product-name">MEROLUX</h2>
        <p class="tagline">Pure Whey Protein Isolate Blend</p>
        <div class="divider"></div>
        <p class="flavour">Banana</p>
      </div>
    </section>
    <section class="lid-label strawberry">
      <div class="lid-face">
        <div class="maker"><span class="maker-dot"></span>VERAFORM</div>
        <h2 class="product-name">MEROLUX</h2>
        <p class="tagline">Pure Whey Protein Isolate Blend</p>
        <div class="divider"></div>
        <p class="flavour">Strawberry</p>
      </div>
    </section>
  </main>
</body>
</html>
```